Catalog design merchandise 2020

We, Lutz Brandauer GmbH, have been producing high-quality cleaning agents for professional users since 1923 and sell them all over Europe.

We need a revision of our merchandise catalog for 2020. The design should be based on our chemical catalog 2019. Please do not submit any designs with chemicals, we need a merchandise catalog !!! Content pages would also be good and not just the front cover. It is not a flyer, but a catalog with about 45-50 pages

Please submit 2-3 design suggestions.

Everything else can then be discussed in detail.

Sincerely yours
marketing department
Lutz Brandauer GmbH

Target Market(s)

Commercial end users (e.g. building cleaners, hotels, industry) for cleaning agents

Font styles to use
Sans Serif

Colors

Designer to choose colors to be used in the design.

Requirements
Must have
• Clear structured design based on the chemistry catalog.
Nice to have
• Loosening up with full pages with pictures (e.g. cleaning car at the airport or vacuum cleaner in the hotel in use)

```html
<!DOCTYPE html>
<html lang="de">
<head>
<meta charset="utf-8">
<title>Lutz Brandauer GmbH – Produktprogramm Reinigungstechnik 2020</title>
<link rel="stylesheet" href="https://fonts.googleapis.com/css2?family=PT+Sans:wght@400;700&display=swap">
<style>
:root{
  --bg:#d9dadc;
  --paper:#ffffff;
  --brand-red:#b4303f;
  --grey:#a7a9ac;
  --ink:#333333;
  --photo-light:#e6ebf0;
  --photo-mid:#b9c6d4;
  --photo-floor:#7f94ab;
}
*{box-sizing:border-box;margin:0;padding:0}
html,body{width:1200px;height:900px;overflow:hidden}
body{background:var(--bg);font-family:"PT Sans",sans-serif;color:var(--ink);position:relative}
.page{position:absolute;background:var(--paper);overflow:hidden;box-shadow:0 2px 6px rgba(0,0,0,.18)}

/* back cover */
.back-cover{left:40px;top:252px;width:280px;height:396px}
.back-cover .photo{position:absolute;left:0;top:0;width:280px;height:322px;
  background:linear-gradient(180deg,var(--photo-light) 0%,var(--photo-mid) 55%,var(--photo-floor) 100%)}
.back-cover .contact-band{position:absolute;left:0;top:334px;width:280px;height:46px;background:var(--brand-red);color:#fff;font-size:6px;line-height:1.35;padding:8px 10px;display:flex;justify-content:space-between}
.back-cover .contact-band strong{font-size:7px}
.back-cover .contact-band .right{text-align:right}

/* front cover */
.front-cover{left:340px;top:252px;width:280px;height:396px}
.front-cover .photo{position:absolute;left:0;top:0;width:280px;height:300px;
  background:linear-gradient(160deg,#f2f4f7 0%,var(--photo-light) 40%,var(--photo-mid) 75%,var(--photo-floor) 100%)}
.brand-mark{position:absolute;right:22px;top:30px;display:flex;align-items:center;gap:5px;color:var(--brand-red);font-weight:700;font-size:20px;letter-spacing:.5px}
.brand-mark .dot{width:9px;height:9px;border-radius:50%;background:var(--brand-red)}
.title-band{position:absolute;left:0;top:312px;width:200px;height:36px;background:var(--brand-red);color:#fff;padding:6px 10px;text-transform:uppercase;line-height:1.2}
.title-band .kicker{font-size:8px;letter-spacing:.6px}
.title-band .headline{font-size:9.5px;font-weight:700;letter-spacing:.4px}
.year-box{position:absolute;left:188px;top:340px;width:92px;height:40px;background:var(--grey);color:#fff;font-size:25px;font-weight:700;display:flex;align-items:center;justify-content:center;letter-spacing:1px}

/* spread */
.spread-left{left:640px;top:262px;width:265px;height:375px}
.spread-right{left:905px;top:262px;width:265px;height:375px;box-shadow:2px 2px 6px rgba(0,0,0,.18)}
.fold{position:absolute;left:897px;top:262px;width:16px;height:375px;background:linear-gradient(90deg,rgba(0,0,0,0) 0%,rgba(0,0,0,.10) 50%,rgba(0,0,0,0) 100%)}
.section-head{position:absolute;top:18px;height:18px;background:var(--brand-red);color:#fff;font-weight:700;font-size:8px;letter-spacing:.5px;display:flex;align-items:center;padding:0 10px;text-transform:uppercase}
.spread-left .section-head{left:0;width:248px}
.spread-right .section-head{right:0;width:236px;justify-content:flex-end}
.product-index{position:absolute;left:14px;top:50px;width:236px;display:grid;grid-template-columns:repeat(3,1fr);column-gap:8px}
.product-index ul{list-style:none}
.product-index li{display:flex;font-size:5.5px;line-height:13px;color:var(--ink)}
.product-index li .name{white-space:nowrap}
.product-index li .leader{flex:1;border-bottom:1px dotted #888;margin:0 2px 4px}
.page-footer{position:absolute;left:0;bottom:10px;width:100%;height:10px;background:var(--grey);color:#fff;font-size:4.5px;display:flex;align-items:center;gap:8px;padding:0 8px;white-space:nowrap}
.page-footer .num{width:16px;height:10px;background:var(--brand-red);color:#fff;font-weight:700;font-size:5.5px;display:flex;align-items:center;justify-content:center;flex:none}
.spread-left .page-footer{padding-left:0}
.spread-right .page-footer{justify-content:flex-end;padding-right:0}

.chapter-list{position:absolute;top:48px;width:112px;list-style:none}
.chapter-list.col-a{left:18px}
.chapter-list.col-b{left:140px}
.chapter-list li{height:13px;margin-bottom:3px;color:#fff;font-size:5.5px;display:flex;align-items:center;justify-content:space-between;padding:0 4px;white-space:nowrap}
.badges{position:absolute;left:18px;top:222px;display:flex;gap:8px;align-items:center}
.badges .badge{width:18px;height:18px;background:#c9cbce}
.badges .badge.round{border-radius:50%}
.imprint{position:absolute;left:0;top:252px;width:265px;height:100px;background:var(--grey);color:#fff;font-size:5px;line-height:1.45;padding:8px 18px;display:grid;grid-template-columns:repeat(3,1fr);gap:6px}
.imprint h3{font-size:6px;font-weight:700}
</style>
</head>
<body>

<section class="page back-cover">
  <div class="photo" role="img" aria-label="Foto: blauer Reinigungswagen mit Wischmopp-Presse und gelbem Warnschild in einem hellen Büroflur mit Zimmerpflanze"></div>
  <div class="contact-band">
    <div><strong>Lutz Brandauer GmbH</strong><br>Werkstraße 14, 91126 Felden<br>Deutschland</div>
    <div class="right">Telefon: +49 0911 / 44 20 0 | Fax: +49 0911 / 44 20 35<br>E-Mail: info@brandauer-reinigung.de | www.brandauer-reinigung.de</div>
  </div>
</section>

<section class="page front-cover">
  <div class="photo" role="img" aria-label="Foto: Reinigungswagen mit Mopp und Nass-Trockensauger in einem hellen Raum"></div>
  <div class="brand-mark"><span class="dot"></span>Brandex</div>
  <div class="title-band">
    <div class="kicker">Produktprogramm</div>
    <div class="headline">Reinigungstechnik &amp; Zubehör</div>
  </div>
  <div class="year-box">2020</div>
</section>

<section class="page spread-left">
  <div class="section-head">Produktverzeichnis</div>
  <div class="product-index">
    <ul>
      <li><span class="name">Abfallsammler</span><span class="leader"></span>44</li>
      <li><span class="name">Arbeitshandschuhe</span><span class="leader"></span>38</li>
      <li><span class="name">Besen</span><span class="leader"></span>12</li>
      <li><span class="name">Bodenwischer</span><span class="leader"></span>8</li>
      <li><span class="name">Dosierpumpe</span><span class="leader"></span>46</li>
      <li><span class="name">Eimer</span><span class="leader"></span>14</li>
      <li><span class="name">Einwegtücher</span><span class="leader"></span>36</li>
      <li><span class="name">Fahreimer</span><span class="leader"></span>15</li>
      <li><span class="name">Fensterabzieher</span><span class="leader"></span>10</li>
      <li><span class="name">Flachmopp</span><span class="leader"></span>9</li>
      <li><span class="name">Gummiwischer</span><span class="leader"></span>11</li>
      <li><span class="name">Handbürste</span><span class="leader"></span>13</li>
    </ul>
    <ul>
      <li><span class="name">Kehrgarnitur</span><span class="leader"></span>12</li>
      <li><span class="name">Klappwischer</span><span class="leader"></span>9</li>
      <li><span class="name">Mikrofasertuch</span><span class="leader"></span>34</li>
      <li><span class="name">Moppbezug</span><span class="leader"></span>16</li>
      <li><span class="name">Moppstiel</span><span class="leader"></span>17</li>
      <li><span class="name">Nass-Trockensauger</span><span class="leader"></span>22</li>
      <li><span class="name">Padhalter</span><span class="leader"></span>24</li>
      <li><span class="name">Poliermaschine</span><span class="leader"></span>26</li>
      <li><span class="name">Moppresse</span><span class="leader"></span>18</li>
      <li><span class="name">Putzwagen</span><span class="leader"></span>19</li>
      <li><span class="name">Reinigungspad</span><span class="leader"></span>25</li>
      <li><span class="name">Scheuerschwamm</span><span class="leader"></span>35</li>
    </ul>
    <ul>
      <li><span class="name">Schrubber</span><span class="leader"></span>13</li>
      <li><span class="name">Sprühflasche</span><span class="leader"></span>47</li>
      <li><span class="name">Staubsauger</span><span class="leader"></span>20</li>
      <li><span class="name">Staubwedel</span><span class="leader"></span>33</li>
      <li><span class="name">Teleskopstange</span><span class="leader"></span>11</li>
      <li><span class="name">Toilettenbürste</span><span class="leader"></span>37</li>
      <li><span class="name">Wandhalter</span><span class="leader"></span>45</li>
      <li><span class="name">Warnschild</span><span class="leader"></span>42</li>
      <li><span class="name">Wäschesack</span><span class="leader"></span>21</li>
      <li><span class="name">Wischmopp</span><span class="leader"></span>8</li>
      <li><span class="name">WC-Garnitur</span><span class="leader"></span>37</li>
      <li><span class="name">Zubehörkorb</span><span class="leader"></span>43</li>
    </ul>
  </div>
  <div class="page-footer"><span class="num">2</span>Telefon: +49 0911 / 44 20 0 | Fax: +49 0911 / 44 20 35 | E-Mail: info@brandauer-reinigung.de</div>
</section>

<section class="page spread-right">
  <div class="section-head">Inhaltsverzeichnis</div>
  <ul class="chapter-list col-a">
    <li style="background:#e3b51d">Moppsysteme<span>6</span></li>
    <li style="background:#4b2f83">Wischgeräte<span>8</span></li>
    <li style="background:#3a57a5">Fensterreinigung<span>10</span></li>
    <li style="background:#1e9a9a">Besen &amp; Bürsten<span>12</span></li>
    <li style="background:#5ea43c">Eimer &amp; Pressen<span>14</span></li>
    <li style="background:#222222">Reinigungswagen<span>18</span></li>
    <li style="background:#6b3b24">Sauger &amp; Maschinen<span>20</span></li>
    <li style="background:#b4303f">Pads &amp; Scheiben<span>24</span></li>
    <li style="background:#f0cf20">Tücher &amp; Schwämme<span>34</span></li>
  </ul>
  <ul class="chapter-list col-b">
    <li style="background:#ec8a1f">Handschuhe<span>38</span></li>
    <li style="background:#9b8cc4">Sicherheit<span>42</span></li>
    <li style="background:#55a9dc">Abfallsysteme<span>44</span></li>
    <li style="background:#e76aa0">Dosiertechnik<span>46</span></li>
    <li style="background:#c2207a">Sprühsysteme<span>47</span></li>
    <li style="background:#3b78b8">Ersatzteile<span>48</span></li>
    <li style="background:#b5b7ba">Sonstiges<span>50</span></li>
  </ul>
  <div class="badges" aria-label="Zertifikate">
    <span class="badge"></span>
    <span class="badge round"></span>
    <span class="badge round"></span>
    <span class="badge round"></span>
    <span class="badge round"></span>
  </div>
  <div class="imprint">
    <div><h3>Impressum</h3>Herausgeber<br>Lutz Brandauer GmbH<br>Werkstraße 14<br>91126 Felden</div>
    <div><h3>Niederlassungen</h3>Vertrieb Süd<br>Telefon: +49 0911 / 44 20 0</div>
    <div><h3>&nbsp;</h3>Vertrieb Nord<br>Fax: +49 0911 / 44 20 35</div>
  </div>
  <div class="page-footer">Telefon: +49 0911 / 44 20 0 | E-Mail: info@brandauer-reinigung.de | www.brandauer-reinigung.de<span class="num">3</span></div>
</section>
<div class="fold"></div>

</body>
</html>
```